I need an out door banner to help me promote my classes, i am a dating coach. i would like to see designs that use the colors. black, yellow, pink, white,orange. colors that attract women. the final design should communicate how women can Reclaim Every Spark, Shine Once More.

Target Market(s)

Bright Mornings After Midnight Storms: Reclaim Every Spark, Shine Once More: Heartfelt Wisdom on Modern Courtship

Industry/Entity Type

dating advice

Logo Text

Heads Up Sisters: Weed out the Narcissist, the abusers, the couch potatoes, the players & the losers...( Expose & Dump his #ss before he destroys your life)

Colors

Designer to choose colors to be used in the design.

Requirements
Nice to have
• Some bold text too
Should not have
• black round

```html
<!DOCTYPE html>
<html lang="en">
<head>
<meta charset="utf-8">
<title>Heads Up Sisters – Dating Coach Banner</title>
<link rel="stylesheet" href="https://fonts.googleapis.com/css2?family=Montserrat:wght@800;900&display=swap">
<style>
  :root {
    --pink: #e6007e;
    --yellow: #fbf500;
    --orange: #ff5b00;
    --black: #0a0a0a;
    --white: #ffffff;
  }
  html, body {
    margin: 0;
    padding: 0;
    width: 1200px;
    height: 1000px;
    overflow: hidden;
    background: var(--white);
  }
  .banner {
    display: block;
    width: 1200px;
    height: 1000px;
  }
  .frame-outer { fill: var(--pink); }
  .frame-inner { fill: var(--yellow); }
  .rule { stroke: var(--pink); stroke-width: 5; }
  .rule-dot { fill: var(--pink); }
  .brand-mark { fill: var(--pink); }
  .brand-name {
    font-family: "Montserrat", sans-serif;
    font-weight: 900;
    fill: var(--black);
  }
  .headline {
    font-family: "Montserrat", sans-serif;
    font-weight: 900;
    fill: var(--black);
  }
  .accent-orange { fill: var(--orange); }
  .accent-pink { fill: var(--pink); }
  .ribbon { fill: var(--pink); }
  .ribbon-text {
    font-family: "Montserrat", sans-serif;
    font-weight: 800;
    fill: var(--white);
  }
</style>
</head>
<body>
<svg class="banner" viewBox="0 0 1200 1000" xmlns="http://www.w3.org/2000/svg">
  <rect class="frame-outer" x="180" y="135" width="840" height="730" rx="78"/>
  <rect class="frame-inner" x="203" y="158" width="794" height="684" rx="58"/>

  <line class="rule" x1="343" y1="218" x2="860" y2="218"/>
  <circle class="rule-dot" cx="343" cy="218" r="10"/>
  <circle class="rule-dot" cx="860" cy="218" r="10"/>

  <g class="brand">
    <circle class="brand-mark" cx="391" cy="378" r="88"/>
    <text class="brand-name" x="510" y="333" font-size="80" textLength="425" lengthAdjust="spacingAndGlyphs">HEADS UP</text>
    <text class="brand-name" x="510" y="452" font-size="80" textLength="425" lengthAdjust="spacingAndGlyphs">SISTERS</text>
  </g>

  <line class="rule" x1="343" y1="517" x2="860" y2="517"/>
  <circle class="rule-dot" cx="343" cy="517" r="10"/>
  <circle class="rule-dot" cx="860" cy="517" r="10"/>

  <text class="headline" x="268" y="612" font-size="54" textLength="664" lengthAdjust="spacingAndGlyphs">Weed out the <tspan class="accent-orange">NARCISSIST</tspan></text>
  <text class="headline" x="270" y="659" font-size="33" textLength="660" lengthAdjust="spacingAndGlyphs">the <tspan class="accent-pink">ABUSERS</tspan>  the <tspan class="accent-pink">COUCH POTATOES</tspan></text>
  <text class="headline" x="270" y="718" font-size="50" textLength="660" lengthAdjust="spacingAndGlyphs">the <tspan class="accent-orange">PLAYERS</tspan> &amp; the <tspan class="accent-orange">LOSERS</tspan></text>

  <polygon class="ribbon" points="272,744 935,744 922,771 935,798 272,798 285,771"/>
  <text class="ribbon-text" x="600" y="778" font-size="19" text-anchor="middle" textLength="598" lengthAdjust="spacingAndGlyphs">Expose &amp; Dump His @ss Before He Destroys Your Life</text>
</svg>
</body>
</html>
```